Information Security Company Business Cards

Using our included logo, we need a business card design. It should have standard contact information such as :

Ravi Kunst
Senior Security Engineer
ravi.kunst@brindale-works.com
866.555.0193

Maybe include the website "www.brindale-works.com" that we will be redesigning soon.??

open to suggestions of course...

Target Market(s)

Our customers are small to large companies. Generally health-care, financial, insurance and the like.

Industry/Entity Type

Business

Font styles to use
Other font styles liked:
• Something that works with the logo

Requirements
Must have
• Colors should flow with the logo if possible. Or at least we think it should.

```html
<!DOCTYPE html>
<html lang="en">
<head>
<meta charset="utf-8">
<title>Brindale Works – Business Cards</title>
<link rel="stylesheet" href="https://fonts.googleapis.com/css2?family=Open+Sans:wght@400&family=Roboto+Condensed:wght@400;700&display=swap">
<style>
  :root {
    --brand-blue: #1f1f9c;
    --brand-grey: #3b3b3e;
    --text-grey: #444448;
    --rule-grey: #9a9a9e;
    --card-white: #ffffff;
    --page-bg: #e9e9ec;
  }
  * { box-sizing: border-box; margin: 0; padding: 0; }
  html, body { width: 1200px; height: 1200px; overflow: hidden; }
  body {
    background: var(--page-bg);
    display: flex;
    flex-direction: column;
    align-items: center;
    justify-content: center;
    gap: 60px;
  }
  .card {
    position: relative;
    width: 860px;
    height: 491px;
    background: var(--card-white);
    box-shadow: 0 2px 10px rgba(0,0,0,0.12);
  }
  .brand {
    position: absolute;
    display: flex;
    align-items: center;
  }
  .brand-ring {
    border-radius: 50%;
    border-style: solid;
    border-color: var(--brand-blue);
    flex: none;
  }
  .brand-name {
    font-family: "Roboto Condensed", sans-serif;
    font-weight: 700;
    color: var(--brand-blue);
    text-transform: uppercase;
    letter-spacing: 0.02em;
    line-height: 0.95;
  }
  /* Front */
  .card-front .brand { left: 170px; top: 50px; gap: 26px; }
  .card-front .brand-ring { width: 150px; height: 150px; border-width: 11px; }
  .card-front .brand-name { font-size: 54px; }
  .holder {
    position: absolute;
    left: 78px;
    top: 352px;
    font-family: "Roboto Condensed", sans-serif;
  }
  .holder-name { font-size: 34px; color: var(--brand-blue); font-weight: 400; }
  .holder-title { font-size: 25px; color: var(--text-grey); margin-top: 6px; }
  .divider {
    position: absolute;
    left: 430px;
    top: 262px;
    width: 3px;
    height: 160px;
    background: var(--rule-grey);
  }
  .contact-list {
    position: absolute;
    left: 462px;
    top: 250px;
    list-style: none;
    font-family: "Open Sans", sans-serif;
    font-size: 24px;
    color: var(--text-grey);
  }
  .contact-item { display: flex; align-items: center; gap: 14px; height: 50px; }
  .contact-icon { width: 22px; height: 22px; flex: none; }
  /* Back */
  .card-back .brand { left: 50%; top: 50%; transform: translate(-50%, -50%); gap: 40px; }
  .card-back .brand-ring { width: 250px; height: 250px; border-width: 16px; }
  .card-back .brand-name { font-size: 86px; }
</style>
</head>
<body>
  <section class="card card-front" aria-label="Business card front">
    <div class="brand">
      <span class="brand-ring"></span>
      <span class="brand-name">Brindale<br>Works</span>
    </div>
    <div class="holder">
      <p class="holder-name">Ravi Kunst</p>
      <p class="holder-title">Senior Security Engineer</p>
    </div>
    <span class="divider"></span>
    <ul class="contact-list">
      <li class="contact-item">
        <svg class="contact-icon" viewBox="0 0 24 24" aria-hidden="true">
          <rect x="2" y="5" width="20" height="14" fill="var(--brand-blue)"/>
          <path d="M2 5 L12 13 L22 5" fill="none" stroke="#fff" stroke-width="1.8"/>
        </svg>
        <span>ravi.kunst@brindale-works.com</span>
      </li>
      <li class="contact-item">
        <svg class="contact-icon" viewBox="0 0 24 24" aria-hidden="true">
          <path fill="var(--brand-blue)" d="M6.6 10.8c1.4 2.8 3.8 5.1 6.6 6.6l2.2-2.2c.3-.3.7-.4 1-.2 1.1.4 2.3.6 3.6.6.6 0 1 .4 1 1V20c0 .6-.4 1-1 1C10.6 21 3 13.4 3 4c0-.6.4-1 1-1h3.5c.6 0 1 .4 1 1 0 1.3.2 2.5.6 3.6.1.3 0 .7-.2 1l-2.3 2.2z"/>
        </svg>
        <span>866.555.0193</span>
      </li>
      <li class="contact-item">
        <svg class="contact-icon" viewBox="0 0 24 24" aria-hidden="true">
          <g fill="none" stroke="var(--brand-blue)" stroke-width="1.8">
            <circle cx="12" cy="12" r="9.5"/>
            <ellipse cx="12" cy="12" rx="4.2" ry="9.5"/>
            <path d="M2.5 12h19M4 7h16M4 17h16"/>
          </g>
        </svg>
        <span>www.brindale-works.com</span>
      </li>
    </ul>
  </section>

  <section class="card card-back" aria-label="Business card back">
    <div class="brand">
      <span class="brand-ring"></span>
      <span class="brand-name">Brindale<br>Works</span>
    </div>
  </section>
</body>
</html>
```